Re design current site.

Redesign of the current site. Like current design But I don't own it so I need a custom design similar to the current one. Want the model pictures to be shown off as they currently do on the home page I want to show off contact info make it very noticeable and readable.
Target Market(s)
Males age 30-60
Number of Pages Required
1 page
Requirements
Must have
- Must show off model pictures on the page. Must show contact info easy to read easy to find.

```html
<!DOCTYPE html>
<html lang="en">
<head>
<meta charset="utf-8">
<title>Velvet Muse Models</title>
<link href="https://fonts.googleapis.com/css2?family=Roboto:wght@400;500;700&family=Dancing+Script:wght@700&display=swap" rel="stylesheet">
<style>
:root{
  --bg:#141416;
  --bg-header:#18181a;
  --card:#2a2a2d;
  --footer:#2a2a2d;
  --red:#e41e26;
  --white:#ffffff;
  --text:#b9b9bd;
  --muted:#86868b;
  --line:#2c2c30;
}
*{margin:0;padding:0;box-sizing:border-box}
html,body{width:878px;height:1200px;overflow:hidden;background:var(--bg)}
body{font-family:"Roboto",sans-serif;color:var(--text);position:relative}
.abs{position:absolute}

.site-header{left:0;top:0;width:878px;height:70px;background:var(--bg-header);border-bottom:1px solid var(--line)}
.brand{left:98px;top:24px;display:flex;align-items:center;gap:8px;font-size:19px;font-weight:400;color:var(--red);letter-spacing:.5px}
.brand-mark{width:12px;height:12px;background:var(--red)}
.contact{left:554px;top:18px}
.contact .phone{font-size:14px;font-weight:700;color:var(--white);letter-spacing:.3px}
.contact .email{font-size:8.5px;color:var(--muted);margin-top:2px}
.btn-booking{left:677px;top:22px;width:102px;height:24px;background:var(--red);color:var(--white);font-size:8.5px;font-weight:700;display:flex;align-items:center;justify-content:center}

.main-nav{left:0;top:70px;width:878px;height:26px;border-bottom:1px solid var(--line);background:var(--bg-header)}
.main-nav ul{list-style:none;display:flex;position:absolute;left:98px;top:7px;font-size:8.8px;font-weight:500;color:#cfcfd3}
.main-nav li{display:flex;align-items:center}
.main-nav li+li::before{content:"";width:1px;height:8px;background:#555;margin:0 12px;transform:skewX(-15deg)}
.main-nav .active{color:var(--red)}

.hero{left:0;top:96px;width:878px;height:350px;
  background:
    radial-gradient(ellipse 260px 120px at 200px 90px,#b9b9bb 0%,#7d7d80 35%,rgba(40,40,42,0) 100%),
    radial-gradient(ellipse 420px 170px at 380px 150px,#6a6a6d 0%,#3a3a3c 45%,rgba(20,20,22,0) 100%),
    linear-gradient(#141416,#1c1c1e 50%,#141416)}
.hero-curve{left:0;top:330px}
.hero-title{left:0;top:300px;width:878px;text-align:center;font-family:"Dancing Script",cursive;font-size:22px;color:var(--white)}
.hero-title em{font-style:normal;color:var(--red)}
.hero-text{left:0;top:339px;width:878px;text-align:center;font-size:8.8px;line-height:14.5px;color:#d5d5d8}

.section-title{font-size:14px;font-weight:500;color:var(--white)}
.models-title{left:98px;top:451px}
.slider-arrows{left:759px;top:454px;display:flex;gap:3px}
.slider-arrows span{width:9px;height:9px;border-radius:50%;border:1px solid #777}
.slider-arrows span.next{border-color:var(--red)}

.model-card{top:497px;width:162px;height:209px;background:var(--card)}
.model-photo{width:162px;height:162px}
.model-name{text-align:center;font-size:10px;font-weight:500;color:var(--white);margin-top:12px}
.model-stats{text-align:center;font-size:7.5px;color:var(--muted);margin-top:6px}

.about-title{left:98px;top:750px}
.about-text{left:98px;top:781px;width:336px;font-size:8.3px;line-height:14.4px;color:#a5a5aa}
.about-text p+p{margin-top:13px}
.btn-explore{left:98px;top:929px;width:81px;height:24px;border:1.5px solid var(--red);color:var(--red);font-size:7.5px;font-weight:700;display:flex;align-items:center;justify-content:center}

.video-panel{left:502px;top:752px;width:277px;height:201px;
  background:
    radial-gradient(ellipse 90px 110px at 185px 60px,#c1161d 0%,#8a0f14 45%,rgba(40,10,12,0) 100%),
    linear-gradient(90deg,#202022 0%,#2e2e30 45%,#2a1a1b 100%)}
.video-caption{left:21px;top:136px;font-size:13px;color:var(--white)}
.video-sub{left:50px;top:156px;font-family:"Dancing Script",cursive;font-size:20px;color:var(--white)}
.play{left:221px;top:139px;width:46px;height:46px;border-radius:50%;background:var(--white);display:flex;align-items:center;justify-content:center}
.play span{width:36px;height:36px;border-radius:50%;background:var(--red);display:flex;align-items:center;justify-content:center}

.ad{top:997px;width:165px;height:44px;display:flex;flex-direction:column;align-items:center;justify-content:center;color:#eee;font-size:7px;font-weight:700;letter-spacing:.6px}
.ad small{font-size:5px;font-weight:400;color:#bbb;margin-top:4px}
.ad-dark{background:linear-gradient(90deg,#3a3a3c,#6a6a6c)}
.ad-warm{background:linear-gradient(90deg,#7a5a4e,#4a3a36)}
.ad-light{background:#f4f4f4;color:#222;flex-direction:row;gap:8px}
.ad-light .ad-photo{width:60px;height:44px;background:linear-gradient(#e9b99a,#c88a6b)}
.ad-light .ad-copy{display:flex;flex-direction:column;align-items:center;font-size:9px;font-weight:500}
.ad-light .ad-copy b{margin-top:3px;background:var(--red);color:#fff;font-size:5px;padding:2px 6px}

.site-footer{left:0;top:1074px;width:878px;height:126px;background:var(--footer)}
.newsletter-title{left:263px;top:20px;font-size:14px;font-weight:500;color:var(--white)}
.newsletter-form{left:398px;top:16px;width:217px;height:24px;display:flex}
.newsletter-form .field{flex:1;background:var(--white);font-size:8px;color:#999;padding-left:11px;display:flex;align-items:center}
.newsletter-form .submit{width:65px;background:var(--red);color:var(--white);font-size:7.5px;font-weight:700;display:flex;align-items:center;justify-content:center}
.footer-links{left:98px;top:64px;width:681px;display:flex}
.footer-links div{flex:1;text-align:center;border-left:1px solid #3a3a3e;padding:4px 0}
.footer-links div:first-child{border-left:none}
.footer-links b{display:block;font-size:9px;font-weight:500;color:var(--white)}
.footer-links span{display:block;font-size:7.5px;color:var(--muted);margin-top:2px}
.copyright{left:98px;top:109px;font-size:8px;color:#6e6e73}
.copyright span{margin-left:10px}
.social{left:750px;top:110px;display:flex;gap:4px}
.social i{width:6px;height:6px;background:#6e6e73;display:block}
</style>
</head>
<body>

<header class="site-header abs">
  <div class="brand abs"><span class="brand-mark"></span>VELVET MUSE MODELS</div>
  <div class="contact abs">
    <div class="phone">555-014-2288</div>
    <div class="email">hello@velvetmuse.test</div>
  </div>
  <div class="btn-booking abs">MAKE A BOOKING</div>
</header>

<nav class="main-nav abs">
  <ul>
    <li class="active">HOME</li>
    <li>BOOKINGS</li>
    <li>RATES</li>
    <li>MODELS</li>
    <li>EMPLOYMENT</li>
    <li>LINKS</li>
  </ul>
</nav>

<section class="hero abs" role="img" aria-label="Black and white glamour photograph of a woman in a lace mask reclining"></section>
<svg class="hero-curve abs" width="878" height="120" viewBox="0 0 878 120">
  <path d="M0,94 Q520,112 878,13 L878,44 Q560,122 0,96 Z" fill="#e41e26"/>
</svg>
<h1 class="hero-title abs">Treat <em>Yourself</em> and We'll Treat <em>You</em></h1>
<p class="hero-text abs">Please contact us about additional models not posted publicly!<br>Male &amp; female couple available as well. Custom clips and videos available for sale!</p>

<h2 class="section-title models-title abs">Velvet Muse Models</h2>
<div class="slider-arrows abs"><span></span><span class="next"></span></div>

<article class="model-card abs" style="left:98px">
  <div class="model-photo" role="img" aria-label="Photo of model Harper in a lace bikini" style="background:radial-gradient(ellipse 60px 80px at 50% 55%,#d9b29c,#a8877a 60%,#7e7c7a)"></div>
  <div class="model-name">Harper</div><div class="model-stats">20 - 5'3 - 120 - 34B</div>
</article>
<article class="model-card abs" style="left:272px">
  <div class="model-photo" role="img" aria-label="Photo of model Brooke wearing sunglasses outdoors" style="background:linear-gradient(#c9d6e2 0%,#a9b4bd 35%,#b78570 60%,#6e3e2c 100%)"></div>
  <div class="model-name">Brooke</div><div class="model-stats">23 - 5'0 - 110 - 34C</div>
</article>
<article class="model-card abs" style="left:445px">
  <div class="model-photo" role="img" aria-label="Photo of model Lana Rae by a pool in a pink bikini" style="background:radial-gradient(ellipse 50px 60px at 55% 70%,#d43cbc,rgba(212,60,188,0) 100%),linear-gradient(#6f8f6a 0%,#c99480 40%,#4aa5c0 100%)"></div>
  <div class="model-name">Lana Rae</div><div class="model-stats">23 - 5'6 - 110 - 32B</div>
</article>
<article class="model-card abs" style="left:618px">
  <div class="model-photo" role="img" aria-label="Mirror selfie photo of model Skye" style="background:radial-gradient(ellipse 55px 75px at 50% 50%,#b08a76,#6a5a55 60%,#2f3f55)"></div>
  <div class="model-name">Skye</div><div class="model-stats">21 - 5'5 - 110 - 32C</div>
</article>

<h2 class="section-title about-title abs">About Us</h2>
<div class="about-text abs">
  <p>VelvetMuse Concierge Service allows clients to request VelvetMuse to search for models in the location you plan on traveling to. We will search and find attractive models for the dates requested. We also verify they are interested in the service you expect/request and that the pictures we have are recent and real.</p>
  <p>Are you looking for the best Miami Escort Services providing incall and outcall serving the Miami, Fort Lauderdale, West Palm Beach &amp; other major city's? If so, then you have come to the right place! With the most beautiful, hot, sexy and sizzling companions in the Miami, Fort Lauderdale &amp; West Palm Beach areas. Click Here to See Our Models!</p>
</div>
<div class="btn-explore abs">EXPORE MORE</div>

<aside class="video-panel abs" role="img" aria-label="Photo of a model in a red dress">
  <div class="video-caption abs">Custom clips and videos</div>
  <div class="video-sub abs">Available for Sale!</div>
  <div class="play abs"><span><svg width="12" height="12" viewBox="0 0 12 12"><path d="M3,1 L11,6 L3,11 Z" fill="#fff"/></svg></span></div>
</aside>

<div class="ad ad-dark abs" style="left:185px" role="img" aria-label="Advertising banner">MEET SECRET SUGAR BABIES<small>HIDDENPERKS.TEST</small></div>
<div class="ad ad-light abs" style="left:357px">
  <div class="ad-photo" role="img" aria-label="Advertising photo"></div>
  <div class="ad-copy">The Sexy<b>Join for Free!</b></div>
</div>
<div class="ad ad-warm abs" style="left:529px" role="img" aria-label="Advertising banner">SPARKR MADE FOR GUYS OVER 30<small>HIDDENPERKS.TEST</small></div>

<footer class="site-footer abs">
  <div class="newsletter-title abs">Join My Newsletter</div>
  <div class="newsletter-form abs"><div class="field">Email Address</div><div class="submit">SUBSCRIBE</div></div>
  <div class="footer-links abs">
    <div><b>Night Match</b><span>Real people real dates</span></div>
    <div><b>HiddenPerks.test</b><span>Find Your Secret GFE</span></div>
    <div><b>HiddenPerks.test</b><span>Sweet Sugar Babies</span></div>
    <div><b>HiddenPerks.test</b><span>GFE With No Strings</span></div>
  </div>
  <div class="copyright abs">© 2017 Velvet Muse Models.<span>Terms Of Use</span><span>Privacy</span></div>
  <div class="social abs"><i></i><i></i><i></i></div>
</footer>

</body>
</html>
```